" Eu tenho uma sala alugada e atendo meus clientes de forma individual. Ajudo eles em temas como Carreira, Relacionamento Amoroso, orientação vocacional, orientação para pais sobre educação de filhos, ajudo pessoas com problemas psicológicos, tais como sindrome do panico, depressão, fobias, entre outros. "

```html
<!DOCTYPE html>
<html lang="pt-BR">
<head>
<meta charset="UTF-8">
<title>Marcela Vianel – Cartão de Visita</title>
<link rel="stylesheet" href="https://fonts.googleapis.com/css2?family=Cinzel:wght@500;600&family=Open+Sans:wght@600;700&display=swap">
<style>
  :root {
    --page: #ecebe8;
    --maroon: #8e2a3e;
    --maroon-deep: #6f1d2e;
    --white: #ffffff;
    --green: #2e8b3e;
    --gold: #b59a62;
    --shadow: rgba(0, 0, 0, 0.18);
  }
  * { margin: 0; padding: 0; box-sizing: border-box; }
  html, body {
    width: 1200px;
    height: 1200px;
    overflow: hidden;
    background: var(--page);
  }
  .stage {
    width: 1200px;
    height: 1200px;
    display: flex;
    flex-direction: column;
    align-items: center;
    justify-content: center;
    gap: 70px;
  }
  .card {
    width: 900px;
    height: 500px;
    border-radius: 6px;
    box-shadow: 0 10px 30px var(--shadow);
    position: relative;
  }

  /* Back side */
  .card--back {
    background: var(--maroon);
    display: flex;
    align-items: center;
    justify-content: center;
  }
  .back-brand {
    text-align: center;
    color: var(--maroon-deep);
  }
  .back-brand__mark {
    width: 34px;
    height: 34px;
    border-radius: 50%;
    background: var(--maroon-deep);
    margin: 0 auto 18px;
  }
  .back-brand__name {
    font-family: 'Cinzel', serif;
    font-weight: 600;
    font-size: 40px;
    letter-spacing: 2px;
  }
  .back-brand__role {
    font-family: 'Cinzel', serif;
    font-weight: 500;
    font-size: 15px;
    letter-spacing: 7px;
    margin-top: 6px;
  }

  /* Front side */
  .card--front {
    background: var(--white);
    padding: 70px 60px 50px;
    display: flex;
    flex-direction: column;
    justify-content: space-between;
  }
  .front-brand {
    text-align: center;
  }
  .front-brand__mark {
    width: 44px;
    height: 44px;
    border-radius: 50%;
    background: var(--gold);
    margin: 0 auto 22px;
  }
  .front-brand__name {
    font-family: 'Cinzel', serif;
    font-weight: 600;
    font-size: 54px;
    letter-spacing: 3px;
    color: var(--green);
    line-height: 1;
  }
  .front-brand__role {
    display: flex;
    align-items: center;
    justify-content: center;
    gap: 14px;
    margin-top: 10px;
    font-family: 'Cinzel', serif;
    font-weight: 500;
    font-size: 16px;
    letter-spacing: 8px;
    color: var(--gold);
  }
  .front-brand__rule {
    width: 130px;
    height: 2px;
    background: var(--gold);
  }
  .contact-list {
    list-style: none;
    display: flex;
    flex-direction: column;
    gap: 14px;
  }
  .contact-list__item {
    display: flex;
    align-items: center;
    gap: 14px;
    font-family: 'Open Sans', sans-serif;
    font-weight: 700;
    font-size: 24px;
    color: var(--green);
  }
  .contact-list__dot {
    width: 26px;
    height: 26px;
    border-radius: 50%;
    background: var(--green);
    flex: none;
  }
</style>
</head>
<body>
  <main class="stage">
    <section class="card card--back" aria-label="Verso do cartão">
      <div class="back-brand">
        <div class="back-brand__mark"></div>
        <p class="back-brand__name">Marcela Vianel</p>
        <p class="back-brand__role">PSICÓLOGA E COACH</p>
      </div>
    </section>

    <section class="card card--front" aria-label="Frente do cartão">
      <div class="front-brand">
        <div class="front-brand__mark"></div>
        <h1 class="front-brand__name">MARCELA VIANEL</h1>
        <p class="front-brand__role">
          <span class="front-brand__rule"></span>
          PSICÓLOGA E COACH
          <span class="front-brand__rule"></span>
        </p>
      </div>
      <ul class="contact-list">
        <li class="contact-list__item"><span class="contact-list__dot"></span>55 011 94725.3180</li>
        <li class="contact-list__item"><span class="contact-list__dot"></span>Coaching e Psicologia Positiva - Marcela Vianel</li>
      </ul>
    </section>
  </main>
</body>
</html>
```